Investment Opportunities

* Need a one page full colour flyer 8.5 inches by 11 inches printed on two sides
* Must be visually appealing using earth tone colours that compliment the logo color
* use creative graphics and icons to support the message

Target Market(s)

investors

Industry/Entity Type

nutraceuticals

```html
<!DOCTYPE html>
<html lang="en">
<head>
<meta charset="utf-8">
<title>NutriVanta Business Plan Flyer</title>
<link href="https://fonts.googleapis.com/css2?family=Open+Sans:wght@400;600;700;800&display=swap" rel="stylesheet">
<style>
:root{
  --bg:#c7c3c2;
  --teal:#14ad92;
  --teal-dark:#0d7f63;
  --photo-a:#0b6e55;
  --photo-b:#19a887;
  --red:#ec1c24;
  --ink:#1b1b1b;
  --white:#ffffff;
}
*{box-sizing:border-box;margin:0;padding:0}
html,body{width:1200px;height:1200px;overflow:hidden}
body{background:var(--bg);font-family:"Open Sans",Arial,sans-serif;color:var(--ink);position:relative}
.page-label{position:absolute;font-size:17px;font-weight:600;color:#111}
.page-label.front{left:264px;top:98px}
.page-label.back{left:843px;top:1121px}
.page{position:absolute;width:874px;height:1132px;background:var(--white);overflow:hidden;transform:scale(.6213);transform-origin:0 0;box-shadow:0 0 10px rgba(0,0,0,.12)}
.page.front{left:38px;top:145px}
.page.back{left:615px;top:387px}
.abs{position:absolute}
.shapes{position:absolute;left:0;top:0}
.brand-name{position:absolute;font-weight:700;color:var(--teal);font-size:30px;letter-spacing:.5px;text-align:center}
.title{left:453px;top:36px;color:var(--white);font-size:49px;font-weight:800;line-height:52px}
.season{color:var(--red);font-size:45px;font-weight:800}
.red-tab{position:absolute;background:var(--red);color:var(--white);font-weight:800;font-size:22px;display:flex;align-items:center}
.bullet-head{position:absolute;font-size:17px;font-weight:800;padding-left:28px}
.bullet-head::before{content:"";position:absolute;left:8px;top:5px;border-left:10px solid var(--red);border-top:6px solid transparent;border-bottom:6px solid transparent}
.check-item{position:absolute;font-size:13px;line-height:15.5px;padding-left:26px}
.check-item::before{content:"✓";position:absolute;left:6px;top:-1px;font-weight:800;font-size:14px}
.overview{left:440px;top:272px;width:397px;height:495px;border:2px solid #333;border-radius:12px;overflow:hidden}
.overview-head{background:var(--teal);color:var(--white);font-weight:800;font-size:22px;line-height:27px;text-align:center;height:74px;padding-top:10px}
.overview-intro{position:absolute;left:22px;top:82px;width:350px;font-size:13px;line-height:15.5px}
.statement{position:absolute;left:88px;width:285px;font-size:13px;line-height:15.5px}
.statement b{font-size:16px;display:block;line-height:18px}
.hex{position:absolute;left:18px;width:54px;height:60px}
.team-band{left:0;top:845px;width:874px;height:222px;background:var(--teal)}
.team-lead{left:47px;top:868px;color:var(--white);font-size:17px;font-weight:700;line-height:21px}
.portrait{position:absolute;width:82px;height:82px;border-radius:50%;top:947px;background:radial-gradient(circle at 50% 40%,#c99b85,#5b3b33)}
.member{position:absolute;top:935px;color:var(--white);font-size:13px;line-height:15.5px}
.member b{font-weight:700}
.tick-dot{display:block;width:18px;height:18px;margin-bottom:4px}
.vsep{position:absolute;width:1px;background:rgba(255,255,255,.7)}
.footer-name{position:absolute;left:0;top:1080px;height:52px;width:330px;background:var(--red);color:var(--white);font-weight:800;font-size:17px;display:flex;align-items:center;padding-left:41px}
.contact{position:absolute;top:1095px;font-size:20px;font-weight:700;display:flex;align-items:center;gap:8px}
.contact.mail{font-size:15px}
.tri-item{position:absolute;font-size:13px;line-height:15.5px;padding-left:30px}
.tri-item::before{content:"";position:absolute;left:2px;top:1px;border-left:11px solid var(--red);border-top:6px solid transparent;border-bottom:6px solid transparent}
.red-check{position:absolute;color:var(--white);font-size:13px;line-height:15.5px;padding-left:36px}
.red-check svg{position:absolute;left:0;top:0}
.fin-label{position:absolute;color:var(--white);font-weight:700;font-size:13px;line-height:15px;padding-left:22px}
.fin-label::before{content:"✓";position:absolute;left:2px;top:-1px;font-weight:800}
.fin-box{position:absolute;border:1px solid rgba(255,255,255,.75);color:var(--white);font-weight:800;font-size:27px;display:flex;align-items:center;justify-content:center;height:38px}
</style>
</head>
<body>

<div class="page-label front">Front Page</div>
<div class="page-label back">Back Page</div>

<!-- FRONT -->
<section class="page front">
  <svg class="shapes" width="874" height="1132" viewBox="0 0 874 1132">
    <defs>
      <linearGradient id="labFront" x1="0" y1="0" x2="1" y2="1">
        <stop offset="0" stop-color="#1fae8c"/><stop offset="1" stop-color="#0a5e48"/>
      </linearGradient>
    </defs>
    <polygon role="img" aria-label="Green-tinted photograph of a scientist handling laboratory test tubes" fill="url(#labFront)"
      points="0,0 874,0 874,155 640,160 622,172 478,172 460,210 378,210 290,120 0,112"/>
    <polyline fill="none" stroke="var(--red)" stroke-width="2.5" points="0,122 290,122 372,224 480,224 496,186 640,186 650,172 874,168"/>
    <circle cx="186" cy="112" r="60" fill="var(--white)"/>
    <polyline fill="none" stroke="var(--teal)" stroke-width="2" points="654,177 830,177"/>
    <circle cx="830" cy="177" r="3" fill="none" stroke="var(--teal)" stroke-width="1.5"/>
    <polyline fill="none" stroke="var(--teal)" stroke-width="1.5" points="492,808 504,822 828,822"/>
    <circle cx="828" cy="822" r="3" fill="none" stroke="var(--teal)" stroke-width="1.5"/>
    <polygon fill="var(--red)" points="70,810 490,810 500,850 45,850"/>
    <polyline fill="none" stroke="var(--red)" stroke-width="2" points="0,1053 158,1053 178,1075 0,1075"/>
    <polygon fill="var(--white)" points="0,1068 874,1068 874,1132 0,1132"/>
    <polyline fill="none" stroke="var(--red)" stroke-width="2.5" points="0,1052 160,1052 176,1070 465,1070 480,1060 874,1060"/>
    <polygon fill="var(--red)" points="0,1080 312,1080 330,1132 0,1132"/>
    <line x1="330" y1="1132" x2="348" y2="1078" stroke="var(--red)" stroke-width="2"/>
  </svg>

  <div class="brand-name" style="left:40px;top:164px;width:290px">NutriVanta</div>
  <h1 class="abs title">BUSINESS PLAN<br>OVERVIEW</h1>
  <div class="abs season" style="left:523px;top:192px">SPRING 2022</div>

  <div class="red-tab" style="left:42px;top:267px;width:384px;height:34px;padding-left:14px">INVESTMENT OPPORTUNITY</div>

  <div class="bullet-head" style="left:42px;top:312px">Problem/opportunity:</div>
  <div class="check-item" style="left:47px;top:350px;width:370px">Infectious disease, cancers, autoimmune disorders, inflammatory conditions, and allergies are increasing, affecting both human and animal populations.</div>
  <div class="check-item" style="left:48px;top:412px;width:370px">There is a significant and growing need for innovative healthful products and services focused on these areas of concern.</div>

  <div class="bullet-head" style="left:42px;top:482px">Solution:</div>
  <div class="check-item" style="left:47px;top:516px;width:370px">Immunoceuticals are one of the emerging treatment options that would address the current unmet need in a more natural manner.</div>
  <div class="check-item" style="left:47px;top:582px;width:370px">NutriVanta Inc. is poised to become the premier provider of research, resources, services and products to take advantage of these growing global market opportunities.</div>

  <div class="bullet-head" style="left:42px;top:671px">Investment opportunity:</div>
  <div class="check-item" style="left:47px;top:706px;width:370px">1000 shares at $1000 per share (total: $1M)</div>
  <div class="check-item" style="left:47px;top:729px;width:370px">Start-up date target: July 1, 2022</div>

  <div class="abs overview">
    <div class="overview-head">NUTRIVANTA COMPANY<br>OVERVIEW</div>
    <p class="overview-intro"><b>The goal of NutriVanta Inc.</b> is to enhance human and animal health through immune-focused testing, manufacturing, and promoting immunoceutical products that aid in the prevention and treatment of infectious diseases and cancers by naturally enhancing immunity.</p>

    <svg class="hex" style="top:193px" viewBox="0 0 54 60"><polygon points="27,0 54,15 54,45 27,60 0,45 0,15" fill="var(--teal)"/><ellipse cx="27" cy="32" rx="14" ry="8" fill="none" stroke="#fff" stroke-width="2.5"/><circle cx="27" cy="32" r="4" fill="#fff"/><path d="M18 20l2 3M27 17v4M36 20l-2 3" stroke="#fff" stroke-width="2"/></svg>
    <div class="statement" style="top:198px"><b>Vision Statement:</b>To educate, empower and equip the global community to achieve health &amp; wellbeing more naturally.</div>

    <svg class="hex" style="top:296px" viewBox="0 0 54 60"><polygon points="27,0 54,15 54,45 27,60 0,45 0,15" fill="var(--teal)"/><circle cx="27" cy="30" r="13" fill="none" stroke="#fff" stroke-width="2.5"/><circle cx="27" cy="30" r="7" fill="none" stroke="#fff" stroke-width="2.5"/><circle cx="27" cy="30" r="2.5" fill="#fff"/></svg>
    <div class="statement" style="top:298px"><b>Mission Statement:</b>To provide research, resources, laboratory services and immunoceutical products that improve the health of all living beings.</div>

    <svg class="hex" style="top:404px" viewBox="0 0 54 60"><polygon points="27,0 54,15 54,45 27,60 0,45 0,15" fill="var(--teal)"/><circle cx="18" cy="22" r="3.5" fill="none" stroke="#fff" stroke-width="2"/><circle cx="27" cy="20" r="3.5" fill="none" stroke="#fff" stroke-width="2"/><circle cx="36" cy="22" r="3.5" fill="none" stroke="#fff" stroke-width="2"/><path d="M12 32q6-6 12 0M21 30q6-6 12 0M30 32q6-6 12 0M12 40h30" fill="none" stroke="#fff" stroke-width="2"/></svg>
    <div class="statement" style="top:406px"><b>Values:</b>Evidence-based research, Innovation, Integrity, Transparency, Team-centred, and Education</div>

    <svg class="abs" style="left:36px;top:260px" width="330" height="20"><polyline points="2,2 14,14 326,14" fill="none" stroke="var(--teal)" stroke-width="1.5"/><circle cx="2" cy="2" r="2.5" fill="var(--teal)"/><circle cx="325" cy="14" r="3" fill="#fff" stroke="var(--teal)" stroke-width="1.5"/></svg>
    <svg class="abs" style="left:36px;top:364px" width="330" height="20"><polyline points="2,14 14,2 326,2" fill="none" stroke="var(--teal)" stroke-width="1.5"/><circle cx="2" cy="14" r="2.5" fill="var(--teal)"/><circle cx="325" cy="2" r="2" fill="#fff" stroke="var(--teal)" stroke-width="1.5"/></svg>
  </div>

  <div class="abs" style="left:110px;top:812px;color:#fff;font-weight:800;font-size:28px">THE SCIENTIFIC TEAM</div>

  <div class="abs team-band"></div>
  <p class="abs team-lead">A core group of highly credentialed, award-winning scientists have been assembled.<br>The three principal scientists leading this company are:</p>

  <div class="portrait" role="img" aria-label="Portrait photo of Dr. Aldo Ferris" style="left:44px"></div>
  <div class="member" style="left:136px"><svg class="tick-dot" viewBox="0 0 18 18"><circle cx="9" cy="9" r="9" fill="var(--red)"/><path d="M5 9l3 3 5-6" stroke="#fff" stroke-width="2" fill="none"/></svg><b>Dr. Aldo Ferris</b><br>(Professor of Viral<br>Immunology and<br>Cancer Biology)</div>
  <div class="vsep" style="left:262px;top:934px;height:92px"></div>
  <div class="portrait" role="img" aria-label="Portrait photo of Dr. Owen Hartley" style="left:274px;background:radial-gradient(circle at 50% 40%,#d6b39c,#1f6bb5 70%)"></div>
  <div class="member" style="left:365px"><svg class="tick-dot" viewBox="0 0 18 18"><circle cx="9" cy="9" r="9" fill="var(--red)"/><path d="M5 9l3 3 5-6" stroke="#fff" stroke-width="2" fill="none"/></svg><b>Dr. Owen Hartley</b><br>(Professor of<br>Immuno-Toxicology<br>and Nutritional<br>Immunology)</div>
  <div class="vsep" style="left:498px;top:934px;height:92px"></div>
  <div class="portrait" role="img" aria-label="Portrait photo of Dr. Clara Voss" style="left:507px;background:radial-gradient(circle at 50% 40%,#d8b17a,#4a2e26 70%)"></div>
  <div class="member" style="left:601px"><svg class="tick-dot" viewBox="0 0 18 18"><circle cx="9" cy="9" r="9" fill="var(--red)"/><path d="M5 9l3 3 5-6" stroke="#fff" stroke-width="2" fill="none"/></svg><b>Dr. Clara Voss</b><br>(Professor of<br>Immunology and<br>Immunogenetics)</div>
  <div class="vsep" style="left:732px;top:934px;height:92px"></div>
  <div class="member" style="left:752px"><svg class="tick-dot" viewBox="0 0 18 18"><circle cx="9" cy="9" r="9" fill="var(--red)"/><path d="M5 9l3 3 5-6" stroke="#fff" stroke-width="2" fill="none"/></svg>Plus three<br>additional<br>supporting<br>scientists</div>

  <div class="footer-name">Dr. Glen Ashby (Board Chair)</div>
  <div class="contact" style="left:349px"><svg width="20" height="20" viewBox="0 0 20 20"><path d="M4 2l3 0 1 4-2 2q2 4 6 6l2-2 4 1v3q-1 2-3 2Q4 17 2 5q0-2 2-3z" fill="var(--red)"/></svg>555-014-2290</div>
  <div class="contact mail" style="left:524px;top:1098px"><svg width="22" height="16" viewBox="0 0 22 16"><rect width="22" height="16" fill="var(--red)"/><path d="M1 1l10 8 10-8" stroke="#fff" stroke-width="1.8" fill="none"/></svg>&nbsp;g.ashby@nutrivanta.co</div>
</section>

<!-- BACK -->
<section class="page back">
  <svg class="shapes" width="874" height="1132" viewBox="0 0 874 1132">
    <defs>
      <linearGradient id="labBack" x1="0" y1="0" x2="1" y2="1">
        <stop offset="0" stop-color="#23b08f"/><stop offset="1" stop-color="#0a5e48"/>
      </linearGradient>
    </defs>
    <polygon role="img" aria-label="Green-tinted photograph of a scientist filling test tubes with a pipette" fill="url(#labBack)"
      points="0,0 874,0 874,258 812,258 792,243 700,243 660,282 470,282 350,165 130,165 108,212 0,212"/>
    <polyline fill="none" stroke="var(--red)" stroke-width="2.5" points="0,222 110,222 130,177 350,177 470,292 660,292 690,253 790,253 810,270 874,270"/>
    <circle cx="238" cy="197" r="60" fill="var(--white)"/>
    <polyline fill="none" stroke="var(--teal)" stroke-width="1.5" points="442,362 456,376 790,376"/>
    <circle cx="442" cy="362" r="2.5" fill="var(--teal)"/><circle cx="790" cy="376" r="3" fill="#fff" stroke="var(--teal)" stroke-width="1.5"/>
    <polygon fill="var(--red)" points="42,360 396,360 420,397 830,397 834,404 64,404"/>
    <line x1="437" y1="424" x2="437" y2="690" stroke="#555" stroke-width="1"/>
    <polygon fill="var(--teal)" points="0,758 874,772 874,1053 0,1053"/>
    <polygon fill="var(--white)" points="432,758 874,758 874,772 432,772"/>
    <polygon fill="var(--red)" points="70,734 405,734 432,778 42,778"/>
    <polyline fill="none" stroke="var(--teal)" stroke-width="1.5" points="480,752 494,765 828,765"/>
    <circle cx="480" cy="752" r="2.5" fill="var(--teal)"/><circle cx="828" cy="765" r="3" fill="#fff" stroke="var(--teal)" stroke-width="1.5"/>
    <polygon fill="var(--red)" points="465,795 810,795 848,838 490,838"/>
    <line x1="437" y1="815" x2="437" y2="1020" stroke="rgba(255,255,255,.7)" stroke-width="1"/>
    <polygon fill="var(--white)" points="0,1053 874,1053 874,1132 0,1132"/>
    <polyline fill="none" stroke="var(--red)" stroke-width="2.5" points="0,1038 138,1038 170,1075 315,1075 330,1058 448,1058 465,1044 874,1044"/>
    <polygon fill="var(--red)" points="0,1080 312,1080 330,1132 0,1132"/>
    <line x1="314" y1="1080" x2="330" y2="1054" stroke="var(--red)" stroke-width="2"/>
  </svg>

  <div class="brand-name" style="left:92px;top:247px;width:292px">NutriVanta</div>
  <div class="abs season" style="left:507px;top:312px">SPRING 2022</div>
  <div class="abs" style="left:82px;top:367px;color:#fff;font-weight:800;font-size:22px">MARKET POTENTIAL</div>

  <div class="tri-item" style="left:42px;top:428px;width:380px">Infectious disease, cancers, autoimmune disorders, inflammatory conditions and allergies are increasing, affecting both human and animal populations.</div>
  <div class="tri-item" style="left:42px;top:484px;width:380px">Current treatments are proving somewhat ineffective. A properly functioning immune system is the key and common thread that helps to keep the body healthy and free of various disorders.</div>
  <div class="tri-item" style="left:42px;top:556px;width:380px">There is increased public awareness regarding new prevention and treatment strategies that rely on more natural approaches to improve human and animal wellbeing.</div>
  <div class="tri-item" style="left:42px;top:629px;width:380px">The solution to these challenges includes developing novel innovative health solutions and products to meet the need.</div>

  <div class="tri-item" style="left:454px;top:428px;width:380px">Immunoceuticals are one of the emerging treatment options that would address the current unmet need.</div>
  <div class="check-item" style="left:481px;top:466px;width:350px">“Immunoceuticals” is a novel term, which means immunological products and systems that naturally improve immuno-competence of an individual.</div>
  <div class="tri-item" style="left:454px;top:522px;width:380px">The immunoceutical space is a unique niche within the nutraceutical industry promoting products that benefit the immunological health.</div>
  <div class="tri-item" style="left:454px;top:579px;width:380px">The Canadian nutraceuticals market (which includes immunoceuticals) is expected to grow 5.62% annually during the period 2019-2024.</div>
  <div class="tri-item" style="left:454px;top:636px;width:380px">Competitors include large pharmaceutical companies and smaller natural product companies with primary distribution channels being health food stores, supermarkets, convenience stores, and direct-to-consumer companies.</div>

  <div class="abs" style="left:100px;top:741px;color:#fff;font-weight:800;font-size:22px">MARKET POTENTIAL</div>

  <div class="red-check" style="left:42px;top:808px;width:380px"><svg width="20" height="20" viewBox="0 0 20 20"><circle cx="10" cy="10" r="10" fill="var(--red)"/><path d="M5.5 10l3 3 6-6.5" stroke="#fff" stroke-width="2.2" fill="none"/></svg>The mandate of the company is to perform research, provide resources and services, and develop, test and market products in the immunoceutical space.</div>
  <div class="red-check" style="left:42px;top:864px;width:380px"><svg width="20" height="20" viewBox="0 0 20 20"><circle cx="10" cy="10" r="10" fill="var(--red)"/><path d="M5.5 10l3 3 6-6.5" stroke="#fff" stroke-width="2.2" fill="none"/></svg>The company will specialize in products and systems that promote human and animal health and wellbeing.</div>
  <div class="red-check" style="left:42px;top:905px;width:380px"><svg width="20" height="20" viewBox="0 0 20 20"><circle cx="10" cy="10" r="10" fill="var(--red)"/><path d="M5.5 10l3 3 6-6.5" stroke="#fff" stroke-width="2.2" fill="none"/></svg>It will also strive to educate the public on how immunoceuticals can bolster natural immunity and thereby help prevent and treat disorders associated with sub-optimal immunity.</div>
  <div class="red-check" style="left:42px;top:977px;width:380px"><svg width="20" height="20" viewBox="0 0 20 20"><circle cx="10" cy="10" r="10" fill="var(--red)"/><path d="M5.5 10l3 3 6-6.5" stroke="#fff" stroke-width="2.2" fill="none"/></svg>Currently under development: a home-test kit for Vitamin D levels for mass distribution</div>

  <div class="abs" style="left:507px;top:801px;color:#fff;font-weight:800;font-size:22px">FINANCIAL PROJECTIONS</div>
  <div class="fin-label" style="left:486px;top:855px">Initial start-up lab<br>equipment Costs:</div>
  <div class="fin-box" style="left:668px;top:852px;width:166px">$325,000</div>
  <div class="fin-label" style="left:486px;top:911px">First 6-month<br>operational Budget:</div>
  <div class="fin-label" style="left:666px;top:909px">First 6-month<br>revenue target is:</div>
  <div class="fin-box" style="left:492px;top:951px;width:166px">$340,000</div>
  <div class="fin-box" style="left:668px;top:951px;width:166px">$200,000</div>
  <div class="fin-label" style="left:488px;top:1005px;font-size:15px">Start-up date target:</div>
  <div class="abs" style="left:690px;top:995px;color:#fff;font-weight:800;font-size:25px">July 1, 2022</div>

  <div class="footer-name">Dr. Glen Ashby (Board Chair)</div>
  <div class="contact" style="left:348px;top:1090px"><svg width="20" height="20" viewBox="0 0 20 20"><path d="M4 2l3 0 1 4-2 2q2 4 6 6l2-2 4 1v3q-1 2-3 2Q4 17 2 5q0-2 2-3z" fill="var(--red)"/></svg>555-014-2290</div>
  <div class="contact mail" style="left:526px;top:1093px"><svg width="22" height="16" viewBox="0 0 22 16"><rect width="22" height="16" fill="var(--red)"/><path d="M1 1l10 8 10-8" stroke="#fff" stroke-width="1.8" fill="none"/></svg>&nbsp;g.ashby@nutrivanta.co</div>
</section>

</body>
</html>
```